Eyecatching Carpentry Business card

I need a business card designed for myself, my company name is Lewis Dunmore Carpentry.
I am based on the south coast of England and I do all aspects of carpentry, including;
skirting
Architraves
kitchens
roof construction
flooring
doors
loft conversions
decking
windows
I currently have no company logo or letter head so I leave all design ideas to designers.
All I ask is that it looks professional and modern.
A logo may be incorporated as well.
My contact details should be on the back, telephone and email.

```html
<!DOCTYPE html>
<html lang="en">
<head>
<meta charset="utf-8">
<title>Lewis Dunmore Carpentry – Business Card</title>
<link href="https://fonts.googleapis.com/css2?family=Cinzel:wght@700;900&family=Oswald:wght@500&display=swap" rel="stylesheet">
<style>
  :root {
    --page: #ffffff;
    --wood-light: #8a8886;
    --wood-mid: #6f6d6b;
    --wood-dark: #545250;
    --engrave: #6b605a;
    --engrave-light: #b9b2ad;
    --engrave-dark: #2e2926;
    --band: #9aa6a8;
    --band-edge: #2f3436;
    --seal: #c8703a;
    --seal-text: #f3dcc4;
  }
  * { box-sizing: border-box; margin: 0; padding: 0; }
  html, body {
    width: 1200px; height: 900px; overflow: hidden;
    background: var(--page);
  }
  .canvas { position: relative; width: 1200px; height: 900px; }

  .card {
    position: absolute;
    overflow: hidden;
  }
  .card--front { left: 15px; top: 35px; width: 695px; height: 405px; }
  .card--back  { left: 440px; top: 468px; width: 735px; height: 412px; }

  .card__wood {
    position: absolute; inset: 0;
    background: linear-gradient(100deg, var(--wood-light) 0%, var(--wood-mid) 35%, var(--wood-dark) 55%, var(--wood-mid) 75%, var(--wood-light) 100%);
  }
  .card__lines { position: absolute; inset: 0; }

  .mark {
    position: absolute;
    display: flex; align-items: center; gap: 12px;
  }
  .mark__dot {
    width: 46px; height: 46px; border-radius: 50%;
    background: var(--seal);
  }
  .mark__name {
    font-family: "Cinzel", serif;
    font-weight: 900;
    font-size: 40px;
    color: var(--seal-text);
    letter-spacing: 2px;
  }
  .card--front .mark { left: 32px; top: 50px; }
  .card--back .mark { left: 280px; top: 90px; }

  .engraved {
    font-family: "Cinzel", serif;
    font-weight: 900;
    text-transform: uppercase;
    color: var(--engrave);
    text-shadow: 1px 1px 0 var(--engrave-dark), -1px -1px 0 var(--engrave-light);
  }
  .card__company {
    position: absolute; left: 30px; top: 136px;
    font-size: 24px; letter-spacing: 4px;
  }
  .contact { position: absolute; left: 30px; }
  .contact--phone { top: 226px; }
  .contact--email { top: 308px; }
  .contact__label, .contact__value {
    display: block; font-size: 24px; letter-spacing: 4px; line-height: 30px;
  }

  .card__slogan {
    position: absolute; left: 120px; top: 215px;
    font-family: "Oswald", sans-serif;
    font-weight: 500;
    font-size: 50px;
    letter-spacing: 2px;
    text-transform: uppercase;
    color: var(--wood-mid);
    text-shadow: 1px 1px 0 var(--engrave-dark), -1px -1px 0 var(--engrave-light);
    transform: rotate(-11deg);
    transform-origin: left center;
    white-space: nowrap;
  }
</style>
</head>
<body>
<main class="canvas">

  <section class="card card--front" aria-label="Card front">
    <div class="card__wood" role="img" aria-label="Grey weathered wooden plank texture"></div>
    <svg class="card__lines" viewBox="0 0 695 405" aria-hidden="true">
      <path d="M700 20 C 600 90, 650 220, 520 290 C 430 340, 380 350, 340 410" fill="none" stroke="#2a2a2a" stroke-width="5"/>
      <path d="M700 20 C 600 90, 650 220, 520 290 C 430 340, 380 350, 340 410" fill="none" stroke="#9a9896" stroke-width="2"/>
    </svg>
    <div class="mark"><span class="mark__dot"></span><span class="mark__name">LDC</span></div>
    <h1 class="card__company engraved">Lewis Dunmore Carpentry</h1>
    <p class="contact contact--phone">
      <span class="contact__label engraved">Telephone:</span>
      <span class="contact__value engraved">888-888-888</span>
    </p>
    <p class="contact contact--email">
      <span class="contact__label engraved">Email:</span>
      <span class="contact__value engraved">hello@lewisdunmore.co.uk</span>
    </p>
  </section>

  <section class="card card--back" aria-label="Card back">
    <div class="card__wood" role="img" aria-label="Grey weathered wooden plank texture"></div>
    <svg class="card__lines" viewBox="0 0 735 412" aria-hidden="true">
      <path d="M0 8 C 200 15, 400 20, 540 50 C 620 65, 680 70, 735 68 L 735 88 C 680 90, 620 85, 540 70 C 400 42, 200 35, 0 28 Z" fill="var(--band)" stroke="var(--band-edge)" stroke-width="2"/>
      <path d="M0 300 C 120 285, 250 295, 400 320 C 550 345, 650 350, 735 345 L 735 372 C 650 377, 550 372, 400 347 C 250 322, 120 312, 0 326 Z" fill="var(--band)" stroke="var(--band-edge)" stroke-width="2"/>
    </svg>
    <div class="mark"><span class="mark__dot"></span><span class="mark__name">LDC</span></div>
    <p class="card__slogan">Lewis Dunmore Carpentry</p>
  </section>

</main>
</body>
</html>
```